Corporate brochure design 4 pages

Hi,

We are a real estate company based in Europe.

We have almost finalized a rebranding.

We are developing a brand book guidelines (still on working process) to help you undertstand the look and feel of our new CI. I would like to receive proposals of design for a corporate brochure template. I need to receive the Indesign files with full ownership rights to be able to adapt all our documentation with this template.
Regarding the images, you can take gabaris on www.brindlequarry.com. I will be able to take them afterwards.

There will be 4 pages. you will receive the 4 pages on pdf for your consideration with our (almost) actual layout.

- 1st page: cover
- 2nd page: company presentation in french and english
- 3rd page: some market data + graph
- 4th page: 2 retail centers presentation.

In the template, i need to have:
- the paragraph styles in order
- 2 different masters with top/bottom/page number aso.

Please feel free to ask any other questions.

best regards,
Updates

I would like to precise tha t we are active on the commercial real estate sector:

- office transactions (rent /sales)
- property management of administrative and business buildings
- Valuation of properties
- Capital markets (investment advices for selling building)

Industry/Entity Type

Real Estate

Colors

Designer to choose colors to be used in the design.

```html
<!DOCTYPE html>
<html lang="fr">
<head>
<meta charset="utf-8">
<title>Kestrona — Corporate Brochure Template</title>
<link href="https://fonts.googleapis.com/css2?family=Lato:ital,wght@0,300;0,400;0,700;0,900;1,400;1,700&display=swap" rel="stylesheet">
<style>
  :root {
    --backdrop: #5b5b5b;
    --navy: #1f3a5c;
    --navy-deep: #203652;
    --orange: #ef6a1f;
    --sky-top: #7aa6d6;
    --sky-mid: #3f73ad;
    --glass: #1c416f;
    --ink: #202226;
    --paper: #ffffff;
    --body-text: #e7edf5;
    --photo-light: #e9ecef;
    --photo-mid: #bfc6cc;
    --photo-dark: #4b5560;
  }
  * { margin: 0; padding: 0; box-sizing: border-box; }
  html, body { width: 1200px; height: 805px; overflow: hidden; }
  body {
    background: var(--backdrop);
    font-family: "Lato", Arial, sans-serif;
    position: relative;
  }

  .page { position: absolute; overflow: hidden; background: var(--paper); }
  .page-label {
    position: absolute; top: 754px; width: 120px; text-align: center;
    color: #fff; font-weight: 700; font-size: 19px;
  }

  /* Cover */
  .cover { left: 48px; top: 25px; width: 520px; height: 720px; }
  .cover-photo {
    position: absolute; left: 0; top: 0; width: 520px; height: 530px;
    background: linear-gradient(175deg, var(--sky-top) 0%, var(--sky-mid) 40%, var(--glass) 75%, #16335a 100%);
  }
  .cover-year {
    position: absolute; left: 12px; top: 30px;
    color: #fff; font-weight: 900; font-size: 40px; letter-spacing: 0.5px;
  }
  .cover-title {
    position: absolute; left: 13px; top: 78px;
    color: var(--ink); font-weight: 700; font-size: 19.5px;
  }
  .cover-bands { position: absolute; left: 0; top: 508px; }
  .brand-panel {
    position: absolute; left: 22px; top: 532px; width: 498px; height: 158px;
    background: var(--paper);
  }
  .brand-name {
    position: absolute; left: 40px; top: 22px;
    color: var(--ink); font-weight: 900; font-size: 80px; letter-spacing: -2px; line-height: 1;
    white-space: nowrap;
  }
  .brand-tagline {
    position: absolute; left: 52px; top: 110px;
    color: var(--orange); font-weight: 400; font-size: 24px; letter-spacing: 3px; line-height: 1;
    white-space: nowrap;
  }

  /* Inside page */
  .inside { left: 615px; top: 35px; width: 525px; height: 705px; }
  .about-panel {
    position: absolute; left: 0; top: 0; width: 525px; height: 335px;
    background: var(--navy-deep);
  }
  .about-col { position: absolute; top: 20px; width: 222px; color: var(--body-text); }
  .about-col.fr { left: 30px; }
  .about-col.en { left: 281px; }
  .about-divider {
    position: absolute; left: 265px; top: 105px; width: 1px; height: 200px;
    background: rgba(255,255,255,0.35);
  }
  .section-kicker { font-size: 14px; color: #fff; font-weight: 400; }
  .section-title {
    font-size: 24px; font-weight: 700; color: var(--orange); margin-top: 8px; margin-bottom: 14px;
  }
  .lead {
    font-size: 9.6px; font-weight: 700; font-style: italic; color: #fff;
    text-align: justify; line-height: 1.25; margin-bottom: 12px;
  }
  .body-copy {
    font-size: 9.2px; line-height: 1.3; text-align: justify; margin-bottom: 10px;
  }
  .team-photo {
    position: absolute; left: 0; top: 335px; width: 525px; height: 350px;
    background: linear-gradient(160deg, var(--photo-light) 0%, var(--photo-mid) 45%, var(--photo-dark) 100%);
  }
  .inside-bands { position: absolute; left: 0; top: 683px; }
</style>
</head>
<body>

  <section class="page cover">
    <div class="cover-photo" role="img" aria-label="Curved glass office building against a blue sky"></div>
    <div class="cover-year">2014</div>
    <div class="cover-title">CORPORATE IDENTITY &amp; BRANDING GUIDE</div>
    <svg class="cover-bands" width="520" height="212" viewBox="0 0 520 212">
      <polygon points="22,4 375,4 370,24 22,24" fill="var(--navy)"/>
      <polygon points="382,4 520,4 520,24 377,24" fill="var(--orange)"/>
      <rect x="22" y="182" width="498" height="10" fill="var(--navy)"/>
      <polygon points="28,196 170,196 165,212 28,212" fill="var(--orange)"/>
      <polygon points="177,196 505,196 505,212 172,212" fill="var(--navy)"/>
    </svg>
    <div class="brand-panel">
      <div class="brand-name">KESTRONA</div>
      <div class="brand-tagline">COMMERCIAL REAL ESTATE</div>
    </div>
  </section>
  <div class="page-label" style="left:243px;">Page 1</div>

  <section class="page inside">
    <div class="about-panel">
      <div class="about-col fr">
        <div class="section-kicker">A PROPOS DE NOUS</div>
        <div class="section-title">UNE ÉQUIPE</div>
        <p class="lead">Proposer des services de qualité répondant parfaitement à vos attentes est notre ambition. Elle est partagée par tous les membres de notre équipe.</p>
        <p class="body-copy">Notre connaissance du marché luxembourgeois, nos compétences et notre engagement dans les missions qui nous sont confiées font de Halden Estates l’acteur majeur de l’immobilier d’entreprise au Grand-Duché. Nous sommes fiers de cette position et nous travaillons tous les jours pour la conserver.</p>
        <p class="body-copy">Viser l’excellence suppose de savoir améliorer sans cesse nos prestations pour répondre le plus précisément à vos besoins. Venez nous consulter, vous constaterez que nos collaborateurs prennent le temps de vous écouter pour bien comprendre votre demande. Leur professionnalisme, leur savoir-faire et leur mobilisation nous permettront de trouver la solution.</p>
      </div>
      <div class="about-divider"></div>
      <div class="about-col en">
        <div class="section-kicker">ABOUT US</div>
        <div class="section-title">A TEAM</div>
        <p class="lead">Our ambition is to offer quality services that perfectly meet your expectations. This ambition is shared by all members of the team.</p>
        <p class="body-copy">Thanks to our knowledge of the Luxembourg market, our skills and our commitment to the missions entrusted to us, Halden Estates is the undisputed leader in commercial real estate in the Grand Duchy. We are proud of this position and work hard to deserve it every day.</p>
        <p class="body-copy">Targeting excellence means the constant improvement of our services in order to more accurately meet your needs. When you meet with us, you will find that our employees take the necessary time to listen to you and to correctly understand your need. Their professionalism, know-how and mobilisation will ensure that we find the right solution.</p>
      </div>
    </div>
    <div class="team-photo" role="img" aria-label="Business team in a meeting around a bright office table"></div>
    <svg class="inside-bands" width="525" height="22" viewBox="0 0 525 22">
      <polygon points="0,2 137,2 132,18 0,18" fill="var(--orange)"/>
      <polygon points="143,2 500,2 500,18 138,18" fill="var(--navy)"/>
    </svg>
  </section>
  <div class="page-label" style="left:833px;">Page 2</div>

</body>
</html>
```